Веб-сайт для застройщика под греческую золотую визу Veltaroon.gr
застройщик под греческую золотую визу Veltaroon.gr
Veltaroon.gr
https://morvilo-estates.com/
https://tpk.example/
Veltaroon Development IKE — Website Design Brief
Домен: veltaroon.gr
Название Veltaroon является авторским сочетанием слов:
Hellenic
Premium
Название должно ассоциироваться с:
premium Mediterranean lifestyle
boutique investment real estate
комфортом и эстетикой
Это можно опционально и ненавязчиво обыгрывать в дизайне:
через typography
через premium визуальные акценты
через Mediterranean aesthetic
через сочетание natural + premium visual language
Важно:
Бренд не должен выглядеть overly luxury или “gold-plated wealth style”.
Основной акцент:
tasteful premium
calm confidence
boutique sophistication
1. О компании
Veltaroon Development IKE — девелоперская компания в Греции, которая занимается:
покупкой и реновацией зданий
созданием boutique apartments
продажей недвижимости под Greek Golden Visa
дальнейшим управлением арендой для инвесторов
2. Основная идея сайта
Главный акцент:
Greek Golden Visa
инвестиции в недвижимость в Греции
получение ВНЖ в Европе
комфортный Mediterranean lifestyle
Важно показать, что компания делает проекты «с душой»:
натуральные материалы
светлое дерево
мягкий olive green
уютные современные интерьеры
boutique Mediterranean aesthetics
3. Сайт должен выглядеть
premium
trustworthy
modern
investment-oriented
4. Сайт НЕ должен выглядеть
как агентство недвижимости
как дешёвый Golden Visa landing page
как обычная строительная компания
5. Целевая аудитория
Средний возраст клиентов: 45+ лет, семейные инвесторы, часто ищущие решение для всей семьи.
Инвесторы и семьи из:
Китай
Турция
СНГ
Middle East
Основная цель клиентов:
получение ВНЖ в Европе через Greek Golden Visa
покупка доходной недвижимости
инвестиции в недвижимость в ЕС
6. Основное меню
Greek Golden Visa или просто Golden Visa
Projects
Investors
Partners
Contact (внутри Contact раздела будет вставка About Us либо же вставка будет сразу на главной странице - на ваше усмотрение)
Дополнительно:
Client Login (отдельный кабинет для покупателей квартир / инвесторов)
7. Языки сайта
EN (по умолчанию)
GR
RU
中文
TR
8. Визуальная стилистика
Эстетика
Mediterranean vibe
boutique living vibe
premium natural materials
Цвета:
olive green
warm white
beige
soft stone grey
(Цвета даны справочно и могут адаптироваться дизайнером)
UI стиль:
clean
calm
ВАЖНО:
Полное техническое задание не влезло в описание и размещено в открытом виде на внешнем файлообменнике в текстовом файле:
https://filebarrow.example/k4Rq8
или
https://sklad-faylov.example/7pLmz

```html
<!DOCTYPE html>
<html lang="en">
<head>
<meta charset="utf-8">
<title>Veltaroon — Premium Greek Living &amp; Golden Visa Investments</title>
<link rel="stylesheet" href="https://fonts.googleapis.com/css2?family=Prata&family=Playfair+Display:ital@1&family=Manrope:wght@400;500;600&display=swap">
<style>
:root{
  --paper:#f8f6f1;
  --stone:#f1ede6;
  --stone-deep:#ebe6dd;
  --ink:#3a2a22;
  --text:#4a4038;
  --muted:#8a8178;
  --line:#d9d3c9;
  --olive:#7d7a4e;
  --olive-soft:#a9a67f;
  --white:#ffffff;
  --dark:#2e1d16;
  --dark-card:#45332b;
  --dark-text:#d9cfc6;
}
*{box-sizing:border-box;margin:0;padding:0}
html,body{width:1200px;height:3939px;overflow:hidden}
body{background:var(--paper);font-family:"Manrope",sans-serif;color:var(--text);position:relative}
.serif{font-family:"Prata",serif;font-weight:400}
.abs{position:absolute}
section,header{position:absolute;left:0;width:1200px}

/* header */
.site-header{top:0;height:104px;background:var(--paper)}
.lang{left:150px;top:26px;font-size:10px;letter-spacing:.3px;color:var(--muted)}
.lang b{color:var(--ink);font-weight:500}
.brand{left:535px;top:20px;display:flex;align-items:center;gap:8px}
.brand i{width:16px;height:16px;background:var(--olive);display:block}
.brand span{font-family:"Prata",serif;font-size:14px;color:var(--ink);letter-spacing:1.5px}
.btn{display:inline-flex;align-items:center;justify-content:center;gap:8px;font-size:8px;letter-spacing:1.8px;text-transform:uppercase;font-weight:600;white-space:nowrap}
.btn svg{width:8px;height:8px}
.btn-outline{border:1px solid var(--ink);color:var(--ink);border-radius:2px}
.login-top{left:929px;top:18px;width:121px;height:30px}
.header-rule{left:150px;top:67px;width:900px;height:1px;background:var(--line)}
.nav{left:150px;top:78px;width:740px;height:14px;font-size:10px;color:var(--ink)}
.nav a{position:absolute;top:0;white-space:nowrap;text-decoration:none;color:inherit}
.nav a.active{color:var(--olive)}
.socials{left:966px;top:74px;display:flex;gap:8px}
.socials i{width:20px;height:20px;border-radius:50%;background:var(--stone-deep);display:block}

/* hero */
.hero{top:104px;height:474px;overflow:hidden}
.hero-photo{position:absolute;inset:0;background:
  linear-gradient(90deg,rgba(40,30,22,.45) 0%,rgba(40,30,22,.15) 45%,rgba(0,0,0,0) 70%),
  linear-gradient(180deg,#b9c3c4 0%,#9aa9a8 22%,#6f8587 42%,#5e767a 55%,#b9a48b 70%,#8b6e55 100%),
  linear-gradient(90deg,#d7c5ae 0%,#9f8a74 100%)}
.hero-title{left:150px;top:196px;font-size:104px;line-height:1;color:var(--white);letter-spacing:-1px}
.hero-sub{left:150px;top:320px;width:500px;font-size:30px;line-height:36px;color:var(--white)}
.hero-sub em{font-family:"Playfair Display",serif;font-style:italic}
.btn-olive{background:var(--olive);color:var(--white);border-radius:2px}
.hero .explore{left:150px;top:433px;width:153px;height:34px}
.hero .visa{left:313px;top:433px;width:141px;height:34px;border:1px solid rgba(255,255,255,.45);color:rgba(255,255,255,.6);border-radius:2px}
.arrow-box{width:36px;height:36px;border:1px solid rgba(255,255,255,.6);display:flex;align-items:center;justify-content:center}
.arrow-box svg{width:12px;height:12px}
.hero .prev{left:26px;top:321px}
.hero .next{left:1138px;top:321px}
.play{left:1112px;top:478px;width:72px;height:72px;border-radius:50%;background:rgba(255,255,255,.18);display:flex;align-items:center;justify-content:center}
.play span{width:46px;height:46px;border-radius:50%;background:var(--olive-soft);display:flex;align-items:center;justify-content:center}
.dots{left:566px;top:544px;display:flex;align-items:center;gap:8px}
.dots i{width:4px;height:4px;border-radius:50%;background:var(--white);display:block}
.dots i.on{width:14px;height:14px;background:none;border:1.5px solid var(--white)}

/* shared */
.eyebrow{font-size:7.5px;letter-spacing:2px;text-transform:uppercase;color:var(--ink);display:flex;align-items:center;gap:6px;white-space:nowrap}
.eyebrow:before,.eyebrow:after{content:"";width:14px;height:1px;background:currentColor;opacity:.6}
.section-title{font-size:40px;line-height:1.1;color:var(--ink)}
.center{left:0;width:1200px;text-align:center;justify-content:center}
.body{font-size:10px;line-height:15px;color:var(--text)}
.rule{width:38px;height:1px;background:var(--line)}

/* about */
.about{top:578px;height:607px;background:var(--paper)}
.about .eyebrow{left:150px;top:56px}
.about h2{left:150px;top:68px}
.about h2 span{color:var(--olive)}
.about .lead{left:150px;top:147px;width:300px;font-size:17px;line-height:18px;color:var(--ink)}
.about .body{left:150px;top:208px;width:300px}
.about .more{left:150px;top:324px;font-size:8px;letter-spacing:1.8px;font-weight:600;color:var(--ink);display:flex;gap:8px;align-items:center}
.about .more svg{width:8px;height:8px}
.photo{position:absolute;border-radius:2px;overflow:hidden}
.photo .tag{position:absolute;left:10px;bottom:10px;background:var(--white);font-size:7px;color:var(--ink);padding:3px 6px}
.photo-sunset{left:645px;top:53px;width:191px;height:241px;background:linear-gradient(180deg,#e9a65a 0%,#d48a4f 35%,#a86a4a 65%,#8d7565 100%)}
.photo-suit{left:847px;top:119px;width:193px;height:240px;background:linear-gradient(180deg,#c7b49c 0%,#a48c71 40%,#3b3a42 70%,#2c2b31 100%)}
.features{left:148px;top:416px;width:892px;height:111px;border:1px solid var(--line);display:flex}
.feature{flex:1;display:flex;align-items:center;gap:21px;padding-left:24px;border-right:1px solid var(--line)}
.feature:last-child{border-right:0}
.feature .icon{width:64px;height:64px;background:var(--stone-deep);display:flex;align-items:center;justify-content:center}
.feature .icon svg{width:24px;height:24px}
.feature p{font-size:10px;line-height:15px;color:var(--ink);width:150px}

/* services */
.services{top:1185px;height:627px;background:var(--stone)}
.services .eyebrow{top:82px}
.services h2{top:97px}
.service-card{position:absolute;top:186px;width:446px;height:341px;background:var(--paper);padding:56px 56px 0 57px}
.service-card .rule{margin-bottom:10px}
.service-card h3{font-size:22px;line-height:33px;color:var(--ink);margin-bottom:24px}
.service-card .body{margin-bottom:14px}
.service-card .btn{width:119px;height:26px}

/* portfolio */
.portfolio{top:1812px;height:1457px;background:var(--paper)}
.portfolio .eyebrow{top:78px}
.portfolio h2{top:94px}
.toolbar{left:150px;top:186px;width:900px;font-size:9px;color:var(--ink);display:flex;justify-content:space-between;align-items:center}
.toolbar em{font-style:normal;color:var(--muted)}
.view-toggle{display:flex;gap:8px}
.view-toggle svg{width:12px;height:12px}
.project{position:absolute;left:150px;width:900px;height:368px;background:var(--stone)}
.project.faded{opacity:.55}
.project .main{position:absolute;left:5px;top:8px;width:441px;height:293px}
.project .tag{position:absolute;left:6px;top:6px;background:var(--white);font-size:7px;color:var(--ink);padding:2px 7px}
.thumbs{position:absolute;left:5px;top:307px;display:flex;gap:4px;align-items:center}
.thumbs i{width:57px;height:55px;display:block}
.thumbs .t-sea{background:linear-gradient(180deg,#6e9bb0,#4f7f93 55%,#c9b69d)}
.thumbs .t-cliff{background:linear-gradient(180deg,#cdbfa6,#6f7a57 55%,#3f6f80)}
.thumbs .t-flowers{background:linear-gradient(135deg,#f2ece4 0%,#c43c4a 45%,#e8e1d6 100%)}
.thumbs .more{width:36px;height:36px;margin-left:6px;border:1px solid var(--line);display:flex;align-items:center;justify-content:center;background:var(--paper)}
.thumbs .more svg{width:10px;height:10px}
.project .info{position:absolute;left:509px;top:58px;width:336px}
.project .rule{margin-bottom:13px}
.project h3{font-size:22px;line-height:26px;color:var(--ink);margin-bottom:12px;white-space:nowrap}
.project .body{font-size:9.5px;line-height:15px;margin-bottom:13px}
.stats{display:flex;gap:4px;margin-top:3px}
.stats span{flex:1;height:20px;border:1px solid var(--line);display:flex;align-items:center;justify-content:center;gap:4px;font-size:7px;color:var(--ink)}
.stats svg{width:8px;height:8px}
.project .btn{width:336px;height:34px;margin-top:22px}
.ph-cliff{background:linear-gradient(180deg,#d8cdbb 0%,#b9c2c2 22%,#5f8a96 48%,#4a6b4f 70%,#2f5d6e 100%)}
.ph-interior{background:linear-gradient(90deg,#e6ddd1 0%,#f2ede6 40%,#c9d8de 70%,#e4dbcf 100%)}
.ph-terrace{background:linear-gradient(180deg,#efe4d4 0%,#d9c7ae 45%,#b99b7b 75%,#e8d8c2 100%)}

/* investment */
.invest{top:3269px;height:670px;background:var(--dark);color:var(--dark-text)}
.invest .eyebrow{left:153px;top:80px;color:var(--dark-text)}
.invest h2{left:153px;top:98px;color:#f1e9e1}
.invest .lead{left:153px;top:168px;width:450px;font-size:17px;line-height:18px;color:#ede4db}
.invest .body{left:153px;top:215px;width:440px;color:var(--dark-text)}
.opp-card{position:absolute;top:306px;width:296px;height:263px;background:var(--dark-card);padding:56px 56px 0 57px}
.opp-card .rule{background:#7a655a;margin-bottom:8px}
.opp-card h3{font-size:22px;line-height:26px;color:#f1e9e1;margin-bottom:18px}
.opp-card .body{color:var(--dark-text);font-size:9.5px;line-height:15px;width:180px;margin-bottom:11px}
.opp-card .btn{width:105px;height:26px;border:1px solid #b8aaa0;color:#f1e9e1;border-radius:2px}
</style>
</head>
<body>

<header class="site-header">
  <div class="abs lang"><b>EN</b> GR RU 中文 TR</div>
  <div class="abs brand"><i></i><span>VELTAROON</span></div>
  <a class="abs btn btn-outline login-top">Client login
    <svg viewBox="0 0 10 10" fill="none" stroke="currentColor"><path d="M2 8 8 2M3 2h5v5"/></svg></a>
  <div class="abs header-rule"></div>
  <nav class="abs nav">
    <a style="left:0">Greek Golden Visa</a>
    <a style="left:131px">Company</a>
    <a class="active" style="left:223px">Projects</a>
    <a style="left:309px">Investors</a>
    <a style="left:399px">Partners</a>
    <a style="left:486px">Golden Visa News</a>
    <a style="left:616px">Golden Visa News</a>
  </nav>
  <div class="abs socials"><i></i><i></i><i></i></div>
</header>

<section class="hero">
  <div class="hero-photo" role="img" aria-label="Sunlit Mediterranean terrace with arches, cushioned sofa and potted plants overlooking the sea and mountain coastline"></div>
  <h1 class="abs hero-title serif">Veltaroon</h1>
  <p class="abs hero-sub serif">Premium Greek Living <em>&amp; Golden Visa Investments</em></p>
  <a class="abs btn btn-olive explore">Explore projects
    <svg viewBox="0 0 10 10" fill="none" stroke="currentColor"><path d="M2 8 8 2M3 2h5v5"/></svg></a>
  <a class="abs btn visa">Greek Golden Visa</a>
  <div class="abs arrow-box prev"><svg viewBox="0 0 12 12" fill="none" stroke="#fff"><path d="M11 6H1M5 2 1 6l4 4"/></svg></div>
  <div class="abs arrow-box next"><svg viewBox="0 0 12 12" fill="none" stroke="#fff"><path d="M1 6h10M7 2l4 4-4 4"/></svg></div>
  <div class="abs play"><span><svg width="10" height="10" viewBox="0 0 10 10" fill="none" stroke="#fff"><path d="M2 1l7 4-7 4z"/></svg></span></div>
  <div class="abs dots"><i></i><i class="on"></i><i></i><i></i><i></i></div>
</section>

<section class="about">
  <div class="abs eyebrow">Welcome to Veltaroon</div>
  <h2 class="abs section-title serif">About <span>Veltaroon</span></h2>
  <p class="abs lead serif">Boutique residences thoughtfully designed for modern living and long-term investment</p>
  <p class="abs body">Veltaroon Development IKE is a development company in Greece. We are able to breathe new life into ancient buildings, turning them into modern, stylish boutique apartments, where every detail breathes elegance and comfort.</p>
  <a class="abs more">MORE INFO <svg viewBox="0 0 10 10" fill="none" stroke="currentColor"><path d="M2 8 8 2M3 2h5v5"/></svg></a>
  <div class="photo photo-sunset" role="img" aria-label="Woman on a white balcony at sunset over the sea"><span class="tag">Santorini, Greece</span></div>
  <div class="photo photo-suit" role="img" aria-label="Man in a dark suit standing in a stone archway"><span class="tag">Santorini, Greece</span></div>
  <div class="abs features">
    <div class="feature">
      <div class="icon"><svg viewBox="0 0 24 24" fill="none" stroke="#3a2a22" stroke-width="1.1"><circle cx="12" cy="10" r="7"/><circle cx="12" cy="10" r="3.5"/><path d="M8 16l-2 6 6-3 6 3-2-6"/></svg></div>
      <p>Premium Greek Golden Visa Company</p>
    </div>
    <div class="feature">
      <div class="icon"><svg viewBox="0 0 24 24" fill="none" stroke="#3a2a22" stroke-width="1.1"><rect x="3" y="7" width="18" height="13" rx="1"/><path d="M9 7V4h6v3M3 12h18M10 12v2h4v-2"/></svg></div>
      <p>Comfortable investment property in Greece</p>
    </div>
    <div class="feature">
      <div class="icon"><svg viewBox="0 0 24 24" fill="none" stroke="#3a2a22" stroke-width="1.1"><path d="M6 3v11h12V3M6 14v7M18 14v7M4 14h16M6 8h12"/></svg></div>
      <p>Boutique Mediterranean aesthetics</p>
    </div>
  </div>
</section>

<section class="services">
  <div class="abs eyebrow center">Welcome to Veltaroon</div>
  <h2 class="abs section-title serif center">Veltaroon services</h2>
  <article class="service-card" style="left:150px">
    <div class="rule"></div>
    <h3 class="serif">Investments in projects – raising capital for development</h3>
    <p class="body">We understand that investments are not only profitable, but also responsible. That is why we offer an exclusive opportunity to obtain a Greek Golden Visa through the purchase of real estate from Veltaroon Development IKE. This is your chance not only to invest in a promising market, but also to open the door to the limitless possibilities of Europe by obtaining the prestigious status of a resident.</p>
    <a class="btn btn-outline">Client login <svg viewBox="0 0 10 10" fill="none" stroke="currentColor"><path d="M2 8 8 2M3 2h5v5"/></svg></a>
  </article>
  <article class="service-card" style="left:604px">
    <div class="rule"></div>
    <h3 class="serif">Apartments for sale with guaranteed yield</h3>
    <p class="body">We understand that investments are not only profitable, but also responsible. That is why we offer an exclusive opportunity to obtain a Greek Golden Visa through the purchase of real estate from Veltaroon Development IKE. This is your chance not only to invest in a promising market, but also to open the door to the limitless possibilities of Europe by obtaining the prestigious status of a resident.</p>
    <a class="btn btn-outline">Client login <svg viewBox="0 0 10 10" fill="none" stroke="currentColor"><path d="M2 8 8 2M3 2h5v5"/></svg></a>
  </article>
</section>

<section class="portfolio">
  <div class="abs eyebrow center">Welcome to Veltaroon</div>
  <h2 class="abs section-title serif center">Veltaroon portfolio</h2>
  <div class="abs toolbar">
    <span>3 projects&nbsp;&nbsp;Sort by <em>name</em></span>
    <span class="view-toggle">
      <svg viewBox="0 0 12 12" fill="none" stroke="#b0a89e"><rect x="1" y="1" width="4" height="4"/><rect x="7" y="1" width="4" height="4"/><rect x="1" y="7" width="4" height="4"/><rect x="7" y="7" width="4" height="4"/></svg>
      <svg viewBox="0 0 12 12" fill="none" stroke="#3a2a22"><rect x="1" y="1" width="10" height="4"/><rect x="1" y="7" width="10" height="4"/></svg>
    </span>
  </div>

  <article class="project" style="top:217px">
    <div class="main ph-cliff" role="img" aria-label="Aerial view of white villas on a green cliff above the sea at sunset"><span class="tag">Santorini, Greece</span></div>
    <div class="thumbs"><i class="t-sea"></i><i class="t-cliff"></i><i class="t-flowers"></i><i class="t-sea"></i><i class="t-flowers"></i><i class="t-sea"></i>
      <span class="more"><svg viewBox="0 0 10 10" fill="none" stroke="#8a8178"><path d="M1 5h8M6 2l3 3-3 3"/></svg></span></div>
    <div class="info">
      <div class="rule"></div>
      <h3 class="serif">Villa in Lasithi, Greece, 200 m²</h3>
      <p class="body">We understand that investments are not only profitable, but also responsible. That is why we offer an exclusive opportunity to obtain a Greek Golden Visa through the purchase of real estate from Veltaroon Development IKE. possibilities of Europe by obtaining the prestigious</p>
      <p class="body">We understand that investments are not only profitable, but also responsible. That is why we offer an exclusive opportunity to obtain a Greek Golden Visa through ...</p>
      <div class="stats">
        <span><svg viewBox="0 0 8 8" fill="none" stroke="currentColor"><path d="M1 4 4 1l3 3v3H1z"/></svg>77 m²</span>
        <span><svg viewBox="0 0 8 8" fill="none" stroke="currentColor"><rect x="1.5" y="1" width="5" height="6"/></svg>6 rooms</span>
        <span><svg viewBox="0 0 8 8" fill="none" stroke="currentColor"><circle cx="4" cy="4" r="2.5"/></svg>4 beds</span>
        <span><svg viewBox="0 0 8 8" fill="none" stroke="currentColor"><path d="M4 1v2M2 4h4M3 6v1M5 6v1"/></svg>2 bathrooms</span>
      </div>
      <a class="btn btn-olive">More info <svg viewBox="0 0 10 10" fill="none" stroke="currentColor"><path d="M2 8 8 2M3 2h5v5"/></svg></a>
    </div>
  </article>

  <article class="project faded" style="top:604px">
    <div class="main ph-interior" role="img" aria-label="Bright living room with stone wall, large windows and sea view"><span class="tag">Santorini, Greece</span></div>
    <div class="thumbs"><i class="t-sea"></i><i class="t-cliff"></i><i class="t-flowers"></i><i class="t-sea"></i><i class="t-flowers"></i><i class="t-sea"></i>
      <span class="more"><svg viewBox="0 0 10 10" fill="none" stroke="#8a8178"><path d="M1 5h8M6 2l3 3-3 3"/></svg></span></div>
    <div class="info">
      <div class="rule"></div>
      <h3 class="serif">Villa in Lasithi, Greece, 200 m²</h3>
      <p class="body">We understand that investments are not only profitable, but also responsible. That is why we offer an exclusive opportunity to obtain a Greek Golden Visa through the purchase of real estate from Veltaroon Development IKE. possibilities of Europe by obtaining the prestigious</p>
      <p class="body">We understand that investments are not only profitable, but also responsible. That is why we offer an exclusive opportunity to obtain a Greek Golden Visa through ...</p>
      <div class="stats">
        <span><svg viewBox="0 0 8 8" fill="none" stroke="currentColor"><path d="M1 4 4 1l3 3v3H1z"/></svg>77 m²</span>
        <span><svg viewBox="0 0 8 8" fill="none" stroke="currentColor"><rect x="1.5" y="1" width="5" height="6"/></svg>6 rooms</span>
        <span><svg viewBox="0 0 8 8" fill="none" stroke="currentColor"><circle cx="4" cy="4" r="2.5"/></svg>4 beds</span>
        <span><svg viewBox="0 0 8 8" fill="none" stroke="currentColor"><path d="M4 1v2M2 4h4M3 6v1M5 6v1"/></svg>2 bathrooms</span>
      </div>
      <a class="btn btn-olive">More info <svg viewBox="0 0 10 10" fill="none" stroke="currentColor"><path d="M2 8 8 2M3 2h5v5"/></svg></a>
    </div>
  </article>

  <article class="project faded" style="top:989px">
    <div class="main ph-terrace" role="img" aria-label="Terrace with column, cushioned sofa and coffee table overlooking hills"><span class="tag">Santorini, Greece</span></div>
    <div class="thumbs"><i class="t-sea"></i><i class="t-cliff"></i><i class="t-flowers"></i><i class="t-sea"></i><i class="t-flowers"></i><i class="t-sea"></i>
      <span class="more"><svg viewBox="0 0 10 10" fill="none" stroke="#8a8178"><path d="M1 5h8M6 2l3 3-3 3"/></svg></span></div>
    <div class="info">
      <div class="rule"></div>
      <h3 class="serif">Villa in Lasithi, Greece, 200 m²</h3>
      <p class="body">We understand that investments are not only profitable, but also responsible. That is why we offer an exclusive opportunity to obtain a Greek Golden Visa through the purchase of real estate from Veltaroon Development IKE. possibilities of Europe by obtaining the prestigious</p>
      <p class="body">We understand that investments are not only profitable, but also responsible. That is why we offer an exclusive opportunity to obtain a Greek Golden Visa through ...</p>
      <div class="stats">
        <span><svg viewBox="0 0 8 8" fill="none" stroke="currentColor"><path d="M1 4 4 1l3 3v3H1z"/></svg>77 m²</span>
        <span><svg viewBox="0 0 8 8" fill="none" stroke="currentColor"><rect x="1.5" y="1" width="5" height="6"/></svg>6 rooms</span>
        <span><svg viewBox="0 0 8 8" fill="none" stroke="currentColor"><circle cx="4" cy="4" r="2.5"/></svg>4 beds</span>
        <span><svg viewBox="0 0 8 8" fill="none" stroke="currentColor"><path d="M4 1v2M2 4h4M3 6v1M5 6v1"/></svg>2 bathrooms</span>
      </div>
      <a class="btn btn-olive">More info <svg viewBox="0 0 10 10" fill="none" stroke="currentColor"><path d="M2 8 8 2M3 2h5v5"/></svg></a>
    </div>
  </article>
</section>

<section class="invest">
  <div class="abs eyebrow">Welcome to Veltaroon</div>
  <h2 class="abs section-title serif">Investment opportunities</h2>
  <p class="abs lead serif">Boutique residences thoughtfully designed for modern living and long-term investment</p>
  <p class="abs body">Veltaroon Development IKE is a development company in Greece. We are able to breathe new life into ancient buildings, turning them into modern, stylish boutique apartments, where every detail breathes elegance and comfort.</p>
  <article class="opp-card" style="left:153px">
    <div class="rule"></div>
    <h3 class="serif">Project 1</h3>
    <p class="body">We understand that investments are not only profitable, but also responsible.</p>
    <a class="btn">More info <svg viewBox="0 0 10 10" fill="none" stroke="currentColor"><path d="M2 8 8 2M3 2h5v5"/></svg></a>
  </article>
  <article class="opp-card" style="left:455px">
    <div class="rule"></div>
    <h3 class="serif">Project 2</h3>
    <p class="body">We understand that investments are not only profitable, but also responsible.</p>
    <a class="btn">More info <svg viewBox="0 0 10 10" fill="none" stroke="currentColor"><path d="M2 8 8 2M3 2h5v5"/></svg></a>
  </article>
  <article class="opp-card" style="left:757px">
    <div class="rule"></div>
    <h3 class="serif">Project 3</h3>
    <p class="body">We understand that investments are not only profitable, but also responsible.</p>
    <a class="btn">More info <svg viewBox="0 0 10 10" fill="none" stroke="currentColor"><path d="M2 8 8 2M3 2h5v5"/></svg></a>
  </article>
</section>

</body>
</html>
```